Los Fogones Ember Poultry MENU!

We are looking for a simple, rustic and modern menu that highlights our passion for healthy and tasty chickens!
We want to highlight our menu but yet keep it very simple.

Attached is info on our logo and our menu information

Target Market(s)

We want to attract all customers but primarily we want to focus on the following 3 markets: Healthy concerned, Food fanatics and Family based.

Industry/Entity Type

Fast Food Restaurant

Requirements
Must have
• We must have our logo on the flyer,
• rustic yet modern
• you must use our colors on the flyer and
• KEEP IT SIMPLE
• Here is our Menu below
• Attached is our final menu we are going to advertise:
• Chicken:
• 1/4 Chicken Dark $6.99
• 1/4 Chicken White $7.99
• 1/2 Chicken white + dark $9.99
• 1/2 chicken all white $10.99
• All come with choice of 2 small sides
• 1 whole chicken family meal ( served with 3 Large sides + 2 liter soda) $23.99
• 2 whole chicken family meal (served with 4 Large sides + 2 liter soda) $33.99
• Extra whole chicken (Chicken only) $13.99
• Sides available with meals:
• - Cilantro infused white rice
• - Hand Cut Fries
• - Hand Cut Sweet potato Fries
• - Yucca
• - Fried Plantains
• - Pinto Beans
• - Black Beans
• - Steamed vegetable medley
• - Cesar Salad
• - Garden Salad
• - House Salad
• - Tortillas
• (reg side: $1.99) Large Side $3.29
• Other Dishes available:
• Lomo Saltado: $12.99
• Pesto Pasta (Tallarin Verde) w/ Steak or 1/4 chicken $ 12.99
• Bistek a lo Pobre: $12.99
• Marcos Treat $12.99 (Chicken filet grilled) w/ salads
• Tallarin Saltado (Garden style pasta) w/ Chicken $11.99, Steak add. $1.49
• Tallarin a la Huancaina $12.99 w/ steak or 1/4 chicken
• Garden Salad ($6.99) Add chicken or steak $1.99
• Cesar Salad ($6.99) Add Chicken or steak $1.99
• House Salad ($6.99) Add chicken or steak $1.99
• DRINKS/DESSERTS:
• - SODAS: REG. $1.99 LARGE 2.59
• - ANDA FIZZ: $1.69 CAN; $1.99 IMPORTED; $2.59 BOTTLE
• - SPECIALTY DRINKS: $2.59
• - ALFAJOR $2.99
• - PERUVIAN FLAN $4.99
• - 3 LECHES $4.99
• (SAVE $1.00 OF ANY DESSERT WITH PURCHASE OF MEAL)
Nice to have
• We would love to see it all in 1 half sheet
Should not have
• can not have too much on it where its confusing.

```html
<!DOCTYPE html>
<html lang="en">
<head>
<meta charset="utf-8">
<title>Los Fogones Ember Poultry Menu</title>
<link rel="stylesheet" href="https://fonts.googleapis.com/css2?family=Alfa+Slab+One&family=Montserrat:wght@400;500;600;700;800&family=Mr+Dafoe&family=Oswald:wght@500&display=swap">
<style>
:root{
  --paper:#ebebea;
  --red:#e8313c;
  --rule:#e99a9e;
  --ink:#2a2a2a;
  --white:#ffffff;
  --pink:#f6d4d5;
}
*{margin:0;padding:0;box-sizing:border-box}
html,body{width:880px;height:1200px;overflow:hidden;background:var(--paper)}
.menu{position:relative;width:880px;height:1200px;overflow:hidden;background:radial-gradient(ellipse at 50% 40%,#f3f3f2 0%,var(--paper) 70%,#e2e2e1 100%);font-family:"Montserrat",sans-serif;color:var(--ink)}
.rule-h{position:absolute;left:0;width:880px;border-top:1px dashed var(--rule)}
.rule-v{position:absolute;top:0;height:1200px;border-left:1px dashed var(--rule)}
.band{position:absolute;left:42px;width:795px;background:var(--red);color:var(--white);font-family:"Alfa Slab One",serif;font-weight:400;text-align:center;letter-spacing:20px;text-indent:20px;white-space:nowrap}
.band-chicken{top:53px;height:56px;font-size:34px;line-height:56px}
.band-family{top:321px;height:55px;font-size:34px;line-height:55px}
.portion{position:absolute;top:123px;width:200px;margin-left:-100px;text-align:center;white-space:nowrap}
.flame{width:50px;height:74px;margin:10px auto 0;background:var(--red);border-radius:50% 50% 50% 50% / 40% 40% 60% 60%;border-top-right-radius:4px;transform:rotate(-8deg);display:flex;align-items:center;justify-content:center}
.flame span{transform:rotate(8deg);font-weight:800;font-size:19px;color:#3a1a1a;margin-top:14px}
.portion-name{font-weight:800;font-size:26px;letter-spacing:1px;margin-top:14px;line-height:28px}
.portion-cut{font-weight:700;font-size:15px;letter-spacing:4px;margin-top:2px;line-height:18px}
.price{font-size:12px;letter-spacing:3px;margin-top:2px;line-height:15px}
.note{position:absolute;left:0;width:880px;text-align:center;font-weight:700;font-size:11px;line-height:13px}
.meal{position:absolute;top:400px;width:320px;margin-left:-160px;text-align:center;white-space:nowrap}
.meal-art{display:flex;justify-content:center;gap:8px;height:58px}
.bird{width:80px;height:52px;border-radius:45% 55% 40% 50%;background:linear-gradient(160deg,var(--pink),#eaa7ab)}
.meal-count{font-weight:800;font-size:21px;margin-top:8px;line-height:24px}
.meal-name{font-weight:800;font-size:26px;letter-spacing:1px;line-height:28px}
.meal-kind{font-weight:700;font-size:15px;letter-spacing:4px;margin-top:2px;line-height:18px}
.meal-serve{font-size:8px;margin-top:3px;line-height:10px}
.script{position:absolute;font-family:"Mr Dafoe",cursive;font-weight:400;color:var(--red);font-size:56px;line-height:1;white-space:nowrap}
.list{position:absolute;list-style:none;font-weight:800;font-size:13px;line-height:13.7px;letter-spacing:.5px;white-space:nowrap}
.list li::before{content:"• "}
.list .indent{padding-left:16px}
.list .indent::before{content:""}
.list .light{font-weight:500}
.side-prices{position:absolute;left:207px;top:650px;font-weight:600;font-size:11.5px;line-height:12px}
.heading{position:absolute;font-family:"Oswald",sans-serif;font-weight:500;color:var(--red);font-size:20px;letter-spacing:.5px;line-height:24px}
.art{position:absolute;left:392px;top:620px;width:424px;height:284px;border-radius:40px;background:radial-gradient(ellipse at 55% 65%,#f2b9bc 0%,#f6dcdd 55%,rgba(235,235,234,0) 80%)}
.small{position:absolute;font-size:11.5px;font-weight:500;line-height:14px;white-space:nowrap}
.brand{position:absolute;left:546px;top:1070px;display:flex;align-items:center;gap:8px;font-weight:700;font-size:17px;color:var(--red);white-space:nowrap}
.brand i{display:block;width:15px;height:15px;border-radius:50%;background:var(--red)}
</style>
</head>
<body>
<main class="menu">
  <div class="rule-h" style="top:53px"></div>
  <div class="rule-h" style="top:321px"></div>
  <div class="rule-h" style="top:604px"></div>
  <div class="rule-h" style="top:1152px"></div>
  <div class="rule-v" style="left:42px"></div>
  <div class="rule-v" style="left:837px"></div>

  <h1 class="band band-chicken">CHICKEN</h1>

  <div class="portion" style="left:142px">
    <div class="flame" role="img" aria-label="Red flame icon"><span>1/4</span></div>
    <div class="portion-name">CHICKEN</div><div class="portion-cut">DARK</div><div class="price">$6.99</div>
  </div>
  <div class="portion" style="left:339px">
    <div class="flame" role="img" aria-label="Red flame icon"><span>1/4</span></div>
    <div class="portion-name">CHICKEN</div><div class="portion-cut">WHITE</div><div class="price">$7.99</div>
  </div>
  <div class="portion" style="left:546px">
    <div class="flame" role="img" aria-label="Red flame icon"><span>1/2</span></div>
    <div class="portion-name">CHICKEN</div><div class="portion-cut">WHITE + DARK</div><div class="price">$9.99</div>
  </div>
  <div class="portion" style="left:734px">
    <div class="flame" role="img" aria-label="Red flame icon"><span>1/2</span></div>
    <div class="portion-name">CHICKEN</div><div class="portion-cut">ALL WHITE</div><div class="price">$10.99</div>
  </div>
  <p class="note" style="top:299px">ALL COME WITH CHOICE OF 2 SMALL SIDES</p>

  <h2 class="band band-family">FAMILY MEAL</h2>

  <div class="meal" style="left:262px">
    <div class="meal-art"><div class="bird" role="img" aria-label="Sketch of a whole roast chicken"></div></div>
    <div class="meal-count">1 WHOLE</div><div class="meal-name">CHICKEN</div>
    <div class="meal-kind">FAMILY MEAL</div>
    <div class="meal-serve">(SERVED WITH 3 LARGE SIDES + 2 LITER SODA)</div>
    <div class="price">$23.99</div>
  </div>
  <div class="meal" style="left:622px">
    <div class="meal-art">
      <div class="bird" role="img" aria-label="Sketch of a whole roast chicken"></div>
      <div class="bird" role="img" aria-label="Sketch of a whole roast chicken"></div>
    </div>
    <div class="meal-count">2 WHOLE</div><div class="meal-name">CHICKEN</div>
    <div class="meal-kind">FAMILY MEAL</div>
    <div class="meal-serve">(SERVED WITH 4 LARGE SIDES + 2 LITER SODA)</div>
    <div class="price">$33.99</div>
  </div>
  <p class="note" style="top:580px">EXTRA WHOLE CHICKEN (CHICKEN ONLY) $13.99</p>

  <h3 class="script" style="left:66px;top:628px">Sides:</h3>
  <p class="side-prices">REG SIDE: $1.99<br>LARGE SIDE $3.29</p>
  <ul class="list" style="left:72px;top:686px">
    <li>CILANTRO INFUSED WHITE RICE</li><li>HAND CUT FRIES</li><li>HAND CUT SWEET POTATO FRIES</li>
    <li>YUCCA</li><li>FRIED PLANTAINS</li><li>PINTO BEANS</li><li>BLACK BEANS</li>
    <li>STEAMED VEGETABLE MEDLEY</li><li>CESAR SALAD</li><li>GARDEN SALAD</li><li>HOUSE SALAD</li><li>TORTILLAS</li>
  </ul>

  <h3 class="heading" style="left:57px;top:856px">OTHER DISHES AVAILABLE:</h3>
  <ul class="list" style="left:72px;top:894px">
    <li>LOMO SALTADO: <span class="light">$12.99</span></li>
    <li>PESTO PASTA (TALLARIN VERDE)</li><li class="indent">W/ STEAK OR 1/4 CHICKEN <span class="light">$ 12.99</span></li>
    <li>BISTEK A LO POBRE: <span class="light">$12.99</span></li>
    <li>MARCOS TREAT <span class="light">$12.99</span></li><li class="indent">(CHICKEN FILET GRILLED) W/ SALADS</li>
    <li>TALLARIN SALTADO (GARDEN STYLE PASTA)</li><li class="indent">W/ CHICKEN <span class="light">$11.99,</span> STEAK ADD <span class="light">$1.49</span></li>
    <li>TALLARIN A LA HUANCAINA <span class="light">$12.99</span></li><li class="indent">W/ STEAK OR 1/4 CHICKEN</li>
  </ul>

  <h3 class="heading" style="left:57px;top:1045px">DRINKS:</h3>
  <ul class="list" style="left:72px;top:1076px">
    <li>SODAS: REG. <span class="light">$1.99</span> LARGE <span class="light">2.59</span></li>
    <li>ANDA FIZZ: <span class="light">$1.69</span> CAN; <span class="light">$1.99</span> IMPORTED; <span class="light">$2.59</span> BOTTLE</li>
    <li>SPECIALTY DRINKS: <span class="light">$2.59</span></li>
  </ul>

  <div class="art" role="img" aria-label="Sketch of chips with dips, a salad bowl and a sauce bottle"></div>

  <h3 class="script" style="left:466px;top:628px">Salads:</h3>
  <ul class="list" style="left:510px;top:686px">
    <li>GARDEN SALAD ($6.99)</li><li>CESAR SALAD ($6.99)</li><li>HOUSE SALAD ($6.99)</li>
  </ul>
  <p class="small" style="left:516px;top:732px;font-weight:600">ADD CHICKEN OR STEAK $1.99</p>

  <h3 class="script" style="left:470px;top:884px">Desserts</h3>
  <ul class="list" style="left:512px;top:944px">
    <li>ALFAJOR <span class="light">$2.99</span></li><li>PERUVIAN FLAN <span class="light">$4.99</span></li><li>3 LECHES <span class="light">$4.99</span></li>
  </ul>
  <p class="small" style="left:498px;top:999px">(SAVE $1.00 OF ANY DESSERT<br>WITH PURCHASE OF MEAL)</p>

  <div class="brand"><i></i>Los Fogones Ember Poultry</div>
</main>
</body>
</html>
```